Lanternfield Golf

I want main multi colored logo, with designer choosing a background of their choice for overall page, and then second upload (logo’s font) underneath, with address logo (but with following added right below phone number along with zip Code):

418 Calloway St
Suite 307C
Jersey City, NJ, 07348

a below a bit further down - to start.

Then we’ll take next steps.

```html
<!DOCTYPE html>
<html lang="en">
<head>
<meta charset="utf-8">
<title>Lanternfield Golf</title>
<link rel="stylesheet" href="https://fonts.googleapis.com/css2?family=Jost:wght@600&family=Didact+Gothic&display=swap">
<style>
  :root {
    --navy: #2d3452;
    --gold: #e2ad22;
    --cream: #f2ede0;
    --cream-edge: #fbf7ec;
  }
  * { box-sizing: border-box; margin: 0; padding: 0; }
  html, body {
    width: 834px;
    height: 1200px;
    overflow: hidden;
    background: var(--cream);
  }
  .page {
    width: 834px;
    height: 1200px;
    display: flex;
    flex-direction: column;
    align-items: center;
    justify-content: center;
    background: var(--cream);
    color: var(--navy);
    text-align: center;
  }
  .brand-mark {
    width: 210px;
    height: 210px;
    border-radius: 50%;
    background: var(--navy);
    margin-bottom: 44px;
  }
  .brand-name {
    font-family: "Jost", sans-serif;
    font-weight: 600;
    font-size: 64px;
    line-height: 1.08;
    letter-spacing: 1px;
    text-transform: uppercase;
    color: var(--navy);
  }
  .contact-button {
    display: inline-flex;
    align-items: center;
    gap: 16px;
    margin-top: 26px;
    padding: 8px 30px 8px 8px;
    background: var(--gold);
    border: 3px solid var(--cream-edge);
    border-radius: 40px;
    box-shadow: 0 0 0 2px var(--gold);
    text-decoration: none;
  }
  .contact-button__icon {
    width: 54px;
    height: 54px;
    flex: none;
  }
  .contact-button__label {
    font-family: "Jost", sans-serif;
    font-weight: 600;
    font-size: 34px;
    letter-spacing: 1px;
    color: #fffaf0;
    text-transform: uppercase;
  }
  .address {
    margin-top: 26px;
    font-family: "Didact Gothic", sans-serif;
    font-style: normal;
    font-size: 34px;
    line-height: 1.3;
    color: var(--navy);
  }
</style>
</head>
<body>
  <main class="page">
    <div class="brand-mark" aria-hidden="true"></div>
    <h1 class="brand-name">Lanternfield<br>Golf</h1>
    <a class="contact-button" href="#contact">
      <svg class="contact-button__icon" viewBox="0 0 54 54" aria-hidden="true">
        <circle cx="27" cy="27" r="27" fill="#2d3452"/>
        <rect x="15" y="18" width="24" height="18" rx="2" fill="#e2ad22"/>
        <path d="M15 20 L27 29 L39 20" fill="none" stroke="#2d3452" stroke-width="2.5" stroke-linejoin="round"/>
      </svg>
      <span class="contact-button__label">Click to Contact</span>
    </a>
    <address class="address" id="contact">
      418 Calloway St<br>
      Suite 307C<br>
      Jersey City, NJ, 07348<br>
      917-555-0148
    </address>
  </main>
</body>
</html>
```